WP website design (Whitlock)

We need a wordpress design for an established auction and real estate company based in Daswon Creek, Canada. The winning design will incorporate a professional color scheme with company logo in a clean layout with specified widgets. The design needs to consider that this will be developed on a responsive theme. Colors will complement logo - red, black and gray.

Industry/Entity Type

Real Estate

Font styles to use
Sans Serif

Requirements
Must have
• Must Have:
the main logo is provided and the 'horse' logo shouldbe incorporated into the hearder or sidebar (either left or right)as well. Contact info should be placed in the header, and footer too: (250) 555-0143
(250) 555-0178
(250) 555-0192
rvm@zorquil.bc.ca

- Navigation:
1) Home 2) Auctions 3) Online Auctions 4) About Us 5) Contact Us

Home Page will have following:
"Family owned and operated with a family guarantee.
Located in Dawson Creek, B.C. Canada

Competitive Rates Bonded & Licensed Livestock Dealers & Auctioneers
All Types of Auction Sales in B.C. & Alberta

Farm, Machinery
Equipment Sales
Household & Estate Sales
Livestock Marketing Consultants
Field Cattle Sales
Livestock Pedigree Sales
Horse Sales Appraisals"

Homepage will have auctions - as at http://brindlevexsales.com/upcoming-auctions/.

Footer will have smaller company logo, credit card logo, and attached association logos and this contact info:
.(620) 555-0117: OFFICE
(620) 555-0164: FAX
hgrup@vxq.com: email
Address: 718 N. Birch Ave., Johnson KS
Mailing Address: PO Box 839, Johnson, KS

Widgets:
1) email sign up 2) News blog widget 3) testimonial blog widget 4) featured auctions widget 5) the 'Gold Peg' logo which is included
Nice to have
• Nice to Have:
- demonstrate the drop-down menu styling, e.g. under Auctions
- Upcoming Auctions
- Past Auctions

```html
<!DOCTYPE html>
<html lang="en">
<head>
<meta charset="utf-8">
<title>Whitlock's Auction Mart Ltd.</title>
<link href="https://fonts.googleapis.com/css2?family=Raleway:wght@400;600;700&family=Open+Sans:wght@400;600;700&family=PT+Serif&display=swap" rel="stylesheet">
<style>
:root{
  --red:#e33034;
  --red-dark:#c8202a;
  --ink:#2b2b2b;
  --panel:#3f3f3f;
  --panel-dark:#333;
  --page:#ececec;
  --card:#f1f1f1;
  --box:#f8f8f8;
  --line:#d9d9d9;
  --text:#333;
  --muted:#555;
}
*{box-sizing:border-box;margin:0;padding:0}
html,body{width:995px;height:1200px;overflow:hidden}
body{position:relative;background:var(--page);font-family:"Open Sans",sans-serif;color:var(--text);font-size:11px}
.abs{position:absolute}

/* header */
.header{left:0;top:0;width:995px;height:149px;background:#f6f5f5;border-bottom:1px solid #ddd}
.brand{left:115px;top:14px;width:120px;text-align:center;font-family:"Raleway",sans-serif;font-weight:700;font-size:15px;line-height:20px;color:var(--ink);letter-spacing:.3px}
.brand-dot{width:14px;height:14px;border-radius:50%;background:var(--red);margin:8px auto 0}
.contact-phone{left:514px;top:42px;font-family:"PT Serif",serif;color:var(--red);font-size:15px;display:flex;align-items:center;gap:9px}
.contact-email{left:663px;top:70px;font-size:12px;color:var(--ink)}
.emblem{left:853px;top:19px;width:35px;height:71px;border-radius:40% 40% 20% 20%;background:linear-gradient(#2a2a2a,#111)}

/* nav */
.nav{left:83px;top:107px;width:830px;height:42px;background:linear-gradient(#e8393c,#d92a2f);border-radius:5px 5px 0 0;display:flex;align-items:center}
.nav a{font-family:"Raleway",sans-serif;color:#fff;text-decoration:none;font-size:12px;height:30px;line-height:30px;border-right:1px solid rgba(255,255,255,.25);text-align:center}
.nav a:last-child{border:none}
.dropdown{left:209px;top:149px;width:162px;background:#3a3a3a;z-index:3}
.dropdown li{list-style:none;height:23px;line-height:23px;padding-left:10px;color:#fff;font-size:10px;border-bottom:1px solid #555}
.dropdown li.active{background:var(--red)}

/* main */
.main{left:83px;top:149px;width:830px;height:915px;background:#fff}
.hero{left:89px;top:156px;width:574px;height:242px;background:linear-gradient(180deg,#9bb7d3 0%,#c9a687 45%,#8a6a52 75%,#7b8a6a 100%)}
.signup{left:667px;top:156px;width:243px;height:242px;background:var(--panel);color:#fff;padding:13px 18px}
.signup h2{font-weight:600;font-size:19px;margin-bottom:14px}
.signup label{display:block;font-size:11px;margin:0 0 8px 2px}
.signup .field{width:190px;height:28px;background:#fff;margin-bottom:12px}
.signup .btn{position:absolute;right:32px;bottom:24px;background:var(--red);border-radius:4px;font-size:13px;padding:4px 8px;letter-spacing:.4px}

.section-title{left:115px;top:421px;font-family:"Raleway",sans-serif;font-size:17px;color:var(--ink)}

.auction{left:113px;width:496px;background:var(--card);border:1px solid #ddd;border-radius:4px;height:269px}
.auction .bar{height:34px;background:var(--red);color:#fff;font-family:"Open Sans",sans-serif;font-weight:600;font-size:14.5px;line-height:34px;padding-left:10px;border-radius:3px 3px 0 0;letter-spacing:.3px}
.thumb{left:6px;top:43px;width:93px;height:87px;background:#fff;border:1px solid #ddd;border-radius:3px;padding:6px}
.thumb .ph{width:100%;height:100%}
.links{left:6px;top:132px;width:93px;height:84px;background:#fff;border:1px solid #ddd;border-radius:3px;padding:3px}
.links .lt{background:var(--panel);color:#fff;font-size:14px;font-weight:600;padding:2px 8px;letter-spacing:1px}
.links .li{display:flex;align-items:center;gap:6px;font-size:10.5px;font-weight:600;margin:8px 0 0 6px}
.links .ic{width:15px;height:9px;background:#222;border-radius:1px}
.box{left:107px;width:382px;background:var(--box);border:1px solid #ddd;border-radius:3px;padding:7px 6px;font-size:10px;line-height:15px}
.info{top:45px;height:90px;text-transform:uppercase}
.info b{font-weight:600}
.info .hl{color:var(--red);font-weight:600}
.live{top:149px;height:104px;font-size:11px}
.live h4{font-weight:600;font-size:11px}
.live .bid{color:var(--red);font-weight:600;text-decoration:underline}

/* sidebar */
.badge{left:712px;top:407px;width:110px;height:52px;border:2px solid #222;background:#fff;display:flex;align-items:center;justify-content:center;gap:6px;font-weight:700;font-size:14px;color:#1d3f8f}
.badge span.sq{width:12px;height:12px;background:var(--red)}
.widget{left:662px;width:221px;background:#f3f3f3;border:1px solid #ddd;border-radius:4px}
.widget .wt{background:var(--panel);color:#fff;font-family:"Open Sans",sans-serif;font-size:12.5px;padding:6px 16px;border-radius:3px 3px 0 0}
.wred{color:var(--red);font-weight:600;font-size:10px}
.wtext{font-size:9.5px;line-height:15px;color:var(--text)}
.news-item{display:flex;gap:9px;margin:10px 0 0 12px}
.news-img{width:73px;height:52px;background:linear-gradient(#b9cbe0,#b0765d 60%,#6a7b55);flex:none}
.quote{margin:8px 10px 0 10px}
.quote .qm{color:#999;font-size:16px;line-height:8px}
.author{margin:-2px 30px 0 0;text-align:right;color:var(--red);font-style:italic;font-size:9.5px}

/* footer */
.footer{left:0;top:1064px;width:995px;height:102px;background:#3d3d3d;border-top:4px solid var(--red)}
.fcontact{left:86px;top:1089px;color:#ddd;font-size:10px;line-height:15px}
.cards{left:410px;top:1105px;display:flex;gap:2px}
.cards span{width:42px;height:25px;border-radius:2px}
.fbrand{left:782px;top:1090px;width:100px;text-align:center;color:#fff;font-family:"Raleway",sans-serif;font-weight:700;font-size:12px;line-height:17px}
.copy{left:0;top:1166px;width:995px;height:34px;background:#2f2f2f;color:#999;font-size:10px;text-align:center;line-height:34px}
</style>
</head>
<body>

<div class="abs header"></div>
<div class="abs brand">WHITLOCK'S AUCTION<br>MART LTD.<div class="brand-dot"></div></div>
<div class="abs contact-phone">
  <svg width="30" height="20" viewBox="0 0 30 20"><path d="M3 6c0-2 2-3 3-2l2 3-2 2c1 3 3 5 6 6l2-2 3 2c1 1 0 3-2 3C8 18 3 13 3 6z" fill="#222"/><rect x="14" y="2" width="15" height="9" rx="4" fill="#222"/></svg>
  <span>(250) 555-0143,&nbsp; 555-0178,&nbsp; 555-0192</span>
</div>
<div class="abs contact-email">Email : rvm@zorquil.bc.ca</div>
<div class="abs emblem" role="img" aria-label="Horse head emblem"></div>

<div class="abs main"></div>
<nav class="abs nav">
  <a style="width:91px">HOME</a>
  <a style="width:125px">AUCTIONS</a>
  <a style="width:176px">ONLINE AUCTIONS</a>
  <a style="width:128px">ABOUT US</a>
  <a style="width:170px">CONTACT US</a>
</nav>

<div class="abs hero" role="img" aria-label="Photo of a brick family home with a double garage and parked cars"></div>
<ul class="abs dropdown">
  <li>Farm, Machinery</li>
  <li class="active">Equipment Sales</li>
  <li>Household &amp; Estate Sales</li>
  <li>Field Cattle Sales</li>
  <li>Livestock Pedigree Sales</li>
  <li>Horse Sales Appraisals</li>
  <li>Livestock Marketing Consultants</li>
</ul>

<div class="abs signup">
  <h2>Email sign-up</h2>
  <label>Your Name</label><div class="field"></div>
  <label>Email Address</label><div class="field"></div>
  <div class="btn">Subscribe</div>
</div>

<h1 class="abs section-title">UPCOMING AUCTIONS</h1>

<article class="abs auction" style="top:463px">
  <div class="bar">TRACTORS NOBLE EDMENTON, ALBERTA</div>
  <div class="abs thumb"><div class="ph" role="img" aria-label="Photo of a red farm tractor on grass" style="background:linear-gradient(#c9d6c2,#b33a33 45%,#5f8a3a)"></div></div>
  <div class="abs links"><div class="lt">LINKS</div><div class="li"><span class="ic"></span>Details</div><div class="li"><span class="ic"></span>Photos</div></div>
  <div class="abs box info">Billings area * crop &amp; timber<br><span class="hl">160± acres land noble county</span>, <b>ok ~ billings area * crop &amp; timber ~ excellent hunting</b><br>Absolute auction<br>Seller: The Harlow Land Trust of Oklahoma</div>
  <div class="abs box live"><h4>LIVE ON-SITE AUCTION WITH ONLINE BIDDING</h4>Begins: &nbsp;Tuesday, March 12, 2013 at 10:00 AM CDT<br><span class="bid">Click Here to Bid Online Now!</span><br><b>Location:</b> &nbsp;See Directions<br>United States Billings, OK 74630</div>
</article>

<article class="abs auction" style="top:752px">
  <div class="bar">HORSES LAND NOBLE EDMENTON, ALBERTA</div>
  <div class="abs thumb"><div class="ph" role="img" aria-label="Photo of horses in an indoor sale arena" style="background:linear-gradient(#3b4a6b,#8a6a45 55%,#a0784e)"></div></div>
  <div class="abs links"><div class="lt">LINKS</div><div class="li"><span class="ic"></span>Details</div><div class="li"><span class="ic"></span>Photos</div></div>
  <div class="abs box info">Billings area * crop &amp; timber<br><span class="hl">160± acres land noble county</span>, <b>ok ~ billings area * crop &amp; timber ~ excellent hunting</b><br>Absolute auction<br>Seller: The Harlow Land Trust of Oklahoma</div>
  <div class="abs box live"><h4>LIVE ON-SITE AUCTION WITH ONLINE BIDDING</h4>Begins: &nbsp;Tuesday, March 12, 2013 at 10:00 AM CDT<br><span class="bid">Click Here to Bid Online Now!</span><br><b>Location:</b> &nbsp;See Directions<br>United States Billings, OK 74630</div>
</article>

<div class="abs badge"><span class="sq"></span>Gold Peg</div>

<aside class="abs widget" style="top:469px;height:198px">
  <div class="wt">FEATURED AUCTIONS</div>
  <div role="img" aria-label="Photo of a large two-storey house under a blue sky" style="margin:9px 0 0 18px;width:175px;height:80px;background:linear-gradient(#5b8fd6,#c9b88a 55%,#6a8f4a)"></div>
  <div class="wred" style="margin:10px 0 0 18px">Ipsum is simply dummy Ipsum is</div>
  <div class="wtext" style="margin:4px 10px 0 19px">Lorem Ipsum is simply dummy text of the printing and typesetting industry. Lorem</div>
  <div class="wred" style="font-style:italic;font-weight:400;text-align:right;margin-right:27px">More Detail</div>
</aside>

<aside class="abs widget" style="top:686px;height:178px">
  <div class="wt">NEWS BLOG</div>
  <div class="news-item"><div class="news-img" role="img" aria-label="Photo of a brick house"></div><div><div class="wred">Ipsum is simply dummy</div><div class="wtext" style="margin-top:4px">Lorem Ipsum is that it<br>has a more-or-less</div></div></div>
  <div class="news-item"><div class="news-img" role="img" aria-label="Photo of a brick house"></div><div><div class="wred">Ipsum is simply dummy</div><div class="wtext" style="margin-top:4px">Lorem Ipsum is that it<br>has a more-or-less</div></div></div>
</aside>

<aside class="abs widget" style="top:883px;height:139px">
  <div class="wt">Clients Testimonials</div>
  <div class="wtext quote"><span class="qm">&ldquo;</span> &nbsp;Lorem Ipsum is simply dummy text of the printing and typesetting industry. Lorem Lorem Ipsum is simply dummy text of the printing and typesetting industry. Lorem Lorem <span class="qm">&rdquo;</span></div>
  <div class="author">Marguerite</div>
</aside>

<footer class="abs footer"></footer>
<div class="abs fcontact">Phone : (250) 555-0143,<br>&nbsp;&nbsp;&nbsp;&nbsp;&nbsp;&nbsp;&nbsp;&nbsp;&nbsp;&nbsp;&nbsp;&nbsp;(250) 555-0178,<br>&nbsp;&nbsp;&nbsp;&nbsp;&nbsp;&nbsp;&nbsp;&nbsp;&nbsp;&nbsp;&nbsp;&nbsp;(250) 555-0192<br><span style="line-height:22px">&nbsp;Email &nbsp;: <span style="font-size:12px">rvm@zorquil.bc.ca</span></span></div>
<div class="abs cards"><span style="background:#dfe3ea"></span><span style="background:#e8a13a"></span><span style="background:#e9e9e9"></span></div>
<div class="abs fbrand">WHITLOCK'S AUCTION<br>MART LTD.</div>
<div class="abs copy">Copyright (c) Whitlock's Auction &nbsp;2014-2015. All Right Reserved</div>

</body>
</html>
```